KORVEL's Sponsorship Showcase Brochure

We're on the hunt for an adept graphic designer to design a 2-4 page brochure that compellingly showcases the sponsorship opportunities at KORVEL, a state-of-the-art, non-profit facility owned by the City of Lawton, OK. This won't be your typical folding brochure but rather 2-4 full pages of engaging visuals and content. At KORVEL, we're more than just a hub for aerospace, defense, and related industries. We're champions of STEM education and connectors between academia and the industry.

Our aim with this brochure is to vividly detail spaces like our convention rooms, conference areas, and outdoor reception zones available for naming rights. Additionally, the specifics of sponsorship levels and their associated costs can be found in the attached Excel file. Ultimately, we want to pique the interest of local businesses, presenting them with these unique, tax-deductible sponsorship opportunities and inspiring them to step forward as key financial sponsors, strengthening our shared dedication to progress and community betterment. The final page of the brochure should guide readers on how to sign up and become a part of our mission.

Target Market(s)

Local businesses in Lawton, OK

Industry/Entity Type

Commercial Real Estate, Community Development

Font styles to use
Sans Serif

Colors
EB3D1F
EC4F4E
F09395
F8D3D4
FCEDEE

Requirements
Must have
• The project requires a 2-4 page non-folding brochure showcasing KORVEL's sponsorship opportunities, detailing the benefits, referencing the attached Excel for sponsorship levels and costs, and providing sign-up instructions on the final page.

```html
<!DOCTYPE html>
<html lang="en">
<head>
<meta charset="utf-8">
<title>KORVEL Corporate Naming Rights Opportunity</title>
<link rel="stylesheet" href="https://fonts.googleapis.com/css2?family=Lilita+One&family=Anton&family=Mulish:wght@400;800;900&display=swap">
<style>
  :root{
    --red:#EB3D1F;
    --coral:#EC4F4E;
    --rose:#F09395;
    --blush:#F8D3D4;
    --mist:#FCEDEE;
    --white:#ffffff;
    --ink:#111111;
  }
  *{margin:0;padding:0;box-sizing:border-box;}
  html,body{width:848px;height:1200px;overflow:hidden;background:var(--white);}
  .brochure{position:relative;width:848px;height:1200px;font-family:"Mulish",sans-serif;color:var(--ink);}

  .hero{position:absolute;left:0;top:0;width:848px;height:396px;background:var(--red);}
  .hero-title{position:absolute;left:0;width:848px;top:44px;text-align:center;
    font-family:"Lilita One",sans-serif;font-size:68px;line-height:62px;color:var(--white);
    text-transform:uppercase;letter-spacing:.5px;}
  .hero-intro{position:absolute;left:38px;top:198px;width:590px;font-weight:900;font-size:19.4px;
    line-height:24.6px;color:var(--white);}
  .badge{position:absolute;left:664px;top:220px;width:146px;height:146px;}

  .benefits-head{position:absolute;left:0;top:396px;width:848px;height:57px;background:var(--mist);
    border-bottom:1px solid var(--rose);display:flex;align-items:center;justify-content:center;}
  .benefits-head h2{font-family:"Anton",sans-serif;font-weight:400;font-size:40px;line-height:1;letter-spacing:2.4px;
    text-transform:uppercase;color:var(--ink);white-space:nowrap;}

  .benefits{position:absolute;left:0;top:453px;width:848px;height:480px;background:var(--blush);
    padding:22px 28px 0 52px;}
  .benefits ul{list-style:none;}
  .benefits li{position:relative;padding-left:22px;font-size:19.9px;line-height:24.6px;}
  .benefits li::before{content:"";position:absolute;left:3px;top:10px;width:5px;height:5px;border-radius:50%;background:var(--ink);}
  .benefits strong{font-weight:800;}

  .call{position:absolute;left:0;top:933px;width:848px;height:126px;background:var(--rose);
    padding:7px 34px 0;text-align:center;color:var(--white);font-weight:800;font-size:19px;line-height:22.4px;}

  .contact{position:absolute;left:0;top:1059px;width:848px;height:141px;background:var(--coral);color:var(--white);}
  .contact-item{position:absolute;font-weight:800;color:var(--white);white-space:nowrap;}
  .icon{position:absolute;}
  .phone{left:111px;top:1090px;font-size:26px;line-height:32px;}
  .web{left:111px;top:1153px;font-size:19px;line-height:24px;}
  .office{left:520px;top:1084px;font-size:19px;line-height:24px;}
  .office-line{position:absolute;left:520px;top:1131px;width:253px;border-top:1.5px solid var(--white);}
  .mail{left:520px;top:1152px;font-size:19px;line-height:24px;}
</style>
</head>
<body>
<main class="brochure">
  <section class="hero">
    <h1 class="hero-title">Corporate Naming<br>Rights Opportunity</h1>
    <p class="hero-intro">We are excited to offer an exclusive opportunity for your company to secure the naming rights for the KORVEL : STEM Center, Convention Center, Outdoor reception Area, and Conference Room, . This prestigious sponsorship will place your brand at the forefront of the region's corporate and professional events, underscoring your commitment to innovation and privacy.</p>
    <svg class="badge" viewBox="0 0 146 146" role="img" aria-label="Your naming rights seal">
      <circle cx="73" cy="73" r="71" fill="var(--white)"/>
    </svg>
  </section>

  <header class="benefits-head"><h2>Benefits of Naming Rights Sponsorship</h2></header>

  <section class="benefits">
    <ul>
      <li><strong>Prominent Brand Exposure:</strong> Your company's name and logo will be prominently displayed as the official naming rights sponsor of the KORVEL Facility, ensuring high visibility during networking events and receptions.</li>
      <li><strong>Networking Opportunities:</strong> Access exclusive networking events hosted in this space, providing unique opportunities to connect with professionals, event organizers, and industry leaders.</li>
      <li><strong>Community Engagement:</strong> Demonstrate your commitment to fostering connections within the community by supporting a space designed for meaningful interactions.</li>
      <li><strong>Versatile Use:</strong> The KORVEL Facility will host a wide range of events, offering your company exposure to diverse audiences and industries.</li>
      <li><strong>Enhanced Brand Image:</strong> Align your brand with a space that promotes relaxation, networking, and leisure, enhancing your company's image as a supporter of work-life balance.</li>
      <li><strong>Privacy Assurance:</strong> Showcase your commitment to ensuring confidential discussions and presentations have a secure and private environment.</li>
      <li><strong>Legacy of Excellence:</strong> Associate your brand with a space that represents cutting-edge technology and fosters successful corporate interactions.</li>
    </ul>
  </section>

  <section class="call">
    <p>JOIN US in shaping the future of education, innovation, and TAKE PART in this transformative journey. CONTACT US today to explore sponsorship opportunities and help us empower the leaders and innovators of tomorrow! We have several sponsorship package options that can be tailored to your interests and abilities ( from $500 up to $25.000 )</p>
  </section>

  <footer class="contact">
    <svg class="icon" style="left:38px;top:20px" width="48" height="48" viewBox="0 0 48 48" fill="none" stroke="var(--white)" stroke-width="2" stroke-linejoin="round">
      <path d="M4 6h40v28H22l-10 10v-10H4z"/>
      <path d="M16 12c-2 0-3 2-2 5 2 6 7 11 13 13 3 1 5 0 5-2l-1-3-5-1-2 2c-3-1-6-4-7-7l2-2-1-5z"/>
    </svg>
    <svg class="icon" style="left:38px;top:84px" width="46" height="46" viewBox="0 0 46 46" fill="none" stroke="var(--white)" stroke-width="2">
      <circle cx="23" cy="23" r="21"/><ellipse cx="23" cy="23" rx="9" ry="21"/>
      <path d="M2 23h42M5 12h36M5 34h36M23 2v42"/>
    </svg>
    <svg class="icon" style="left:437px;top:15px" width="56" height="56" viewBox="0 0 56 56" fill="none" stroke="var(--white)" stroke-width="2">
      <circle cx="28" cy="28" r="26"/>
      <path d="M28 40c-6-7-9-11-9-15a9 9 0 0 1 18 0c0 4-3 8-9 15z"/><circle cx="28" cy="25" r="3"/>
      <path d="M21 39c-2 1 0 3 7 3s9-2 7-3"/>
    </svg>
    <svg class="icon" style="left:441px;top:92px" width="48" height="34" viewBox="0 0 48 34" fill="none" stroke="var(--white)" stroke-width="2" stroke-linejoin="round">
      <rect x="1" y="1" width="46" height="32"/><path d="M1 1l23 19L47 1M1 33l17-16M47 33L30 17"/>
    </svg>
  </footer>
  <div class="contact-item phone">+1580555014</div>
  <div class="contact-item web">www.korvel.com</div>
  <div class="contact-item office">Office :</div>
  <div class="office-line"></div>
  <div class="contact-item mail">contactkorvel@korvel.com</div>
</main>
</body>
</html>
```